Harrowfield Bowls Union

I am looking to develop a sponsorship proposal using some of the imagery and colours 'black and gold' into a classy, professional laid out document to present to potential sponsors.
The content for the proposal/presentation is detailed in the "HBU Sponsor Deck". The HBU logo is featured in the black & gold presentations.

```html
<!DOCTYPE html>
<html lang="en">
<head>
<meta charset="utf-8">
<title>HBU Sponsor Deck</title>
<link href="https://fonts.googleapis.com/css2?family=Sora:wght@600;700;800&family=Inter:wght@400;500;600&display=swap" rel="stylesheet">
<style>
:root{
  --page:#ffffff;
  --slide:#0d0b09;
  --gold:#d59a4e;
  --gold-soft:#b97a36;
  --text:#ffffff;
  --muted:#d9d4cc;
  --card:rgba(120,112,104,.42);
  --card-line:rgba(255,255,255,.22);
}
*{margin:0;padding:0;box-sizing:border-box}
html,body{width:856px;height:1200px;overflow:hidden;background:var(--page)}
body{position:relative;font-family:"Inter",sans-serif;color:var(--text)}
.slide{position:absolute;width:387px;height:218px;background:var(--slide);overflow:hidden}
.col-l{left:33px}.col-r{left:436px}
.row-1{top:31px}.row-2{top:260px}.row-3{top:490px}.row-4{top:720px}.row-5{top:951px}
.glow{position:absolute;border-radius:50%;filter:blur(10px);pointer-events:none}
.abs{position:absolute}
.heading{font-family:"Sora",sans-serif;font-weight:700;letter-spacing:-.04em;line-height:1.05;color:var(--text)}
.body{font-size:4px;line-height:1.55;color:var(--muted)}
.body p+p{margin-top:4px}
.photo{position:absolute;border-radius:9px}
.card{position:absolute;background:var(--card);border:.5px solid var(--card-line);border-radius:7px}
.gold{color:var(--gold)}
.presented{position:absolute;right:21px;text-align:right;font-size:3.8px;color:var(--muted)}
.presented b{display:block;margin-top:2px;font-size:4.4px;color:var(--text);font-weight:600;letter-spacing:.02em}
/* cover */
.brand{left:22px;top:27px;font-family:"Inter",sans-serif;font-weight:500;font-size:10px;color:var(--gold-soft);letter-spacing:.01em}
.cover-title{left:22px;top:60px;font-size:25px}
.cover-note{left:22px;top:180px;width:115px;font-size:4px;line-height:1.5;color:var(--muted)}
/* principles */
.principle{display:flex;align-items:center;gap:7px;padding:0 8px}
.principle .num{font-family:"Sora",sans-serif;font-weight:600;font-size:13px;letter-spacing:-.02em;color:var(--text)}
.principle p{font-size:3.8px;line-height:1.5;color:var(--muted)}
/* bullets */
.list{list-style:none;font-size:4px;line-height:1.55;color:var(--muted)}
.list li{position:relative;padding-left:5px}
.list li::before{content:"•";position:absolute;left:0}
.sub{font-size:4px;color:var(--gold)}
/* org chart */
.node{position:absolute;background:rgba(120,112,104,.55);border:.5px solid var(--card-line);border-radius:3px;font-size:3.8px;line-height:1.4;color:var(--text);display:flex;align-items:center;justify-content:center;text-align:center;padding:0 3px}
/* sponsors */
.sponsors{position:absolute;background:#fff;border-radius:3px;display:grid;grid-template-columns:repeat(4,1fr);align-items:center;justify-items:center;padding:8px 10px;row-gap:8px}
.sponsor{font-family:"Inter",sans-serif;font-weight:600;font-size:6px;color:#2b2b2b}
.contact{font-size:6px;line-height:1.55;color:var(--text)}
</style>
</head>
<body>

<!-- Cover -->
<section class="slide col-l row-1">
  <div class="glow" style="left:200px;top:70px;width:170px;height:70px;background:radial-gradient(ellipse,rgba(213,154,78,.45),transparent 70%);transform:rotate(-25deg)"></div>
  <div class="abs brand">Harrowfield Bowls Union</div>
  <h1 class="abs heading cover-title">Live your <span class="gold">Cricket</span><br>Dream</h1>
  <p class="abs cover-note">This proposal details a range of assets that we hope meet and complement the objectives of both your company and HGS Cricket .</p>
  <div class="presented" style="top:182px">Presented by :<b>HARROWFIELD BOWLS UNION</b></div>
</section>

<!-- Who we are -->
<section class="slide col-r row-1">
  <div class="glow" style="left:290px;top:30px;width:90px;height:110px;background:radial-gradient(ellipse,rgba(213,154,78,.5),transparent 70%)"></div>
  <div class="photo" role="img" aria-label="Stadium grandstand at sunset" style="left:22px;top:-10px;width:124px;height:99px;background:linear-gradient(180deg,#d98a5a 0%,#c49a80 45%,#5f7a48 75%,#3f6b2e 100%)"></div>
  <div class="photo" role="img" aria-label="Stadium under lights at night" style="left:22px;top:110px;width:124px;height:118px;background:linear-gradient(180deg,#101826 0%,#2a3a2a 35%,#3f8a3a 60%,#5a3a3a 100%)"></div>
  <h2 class="abs heading" style="left:158px;top:18px;font-size:23px">Who We Are</h2>
  <div class="abs body" style="left:158px;top:50px;width:180px">
    <p>The Harrowfield Bowls Union (HBU) was founded in 1897 (formerly Elmsworth District Cricket Club). The community based club consists of a men's &amp; women's division (senior &amp; youth) competing in the Metro Premier Cricket competition.</p>
    <p>The HBU is 'grass roots' community cricket based at Kestrel Park Oval (home since 1947) and the club seeks the support of local businesses to help us maintain connection with our Inner West - our home base.</p>
    <p>The HBU also has the unique position of being aligned to the Harrowfield Grand Stadium.</p>
    <p>September 2022 - 125 years celebration of this foundation legendary cricket club.</p>
  </div>
  <div class="photo" role="img" aria-label="Women's team group photo with trophy" style="left:158px;top:130px;width:196px;height:86px;background:linear-gradient(180deg,#3b4a32 0%,#2a2a22 40%,#1c1a16 70%,#4f6e35 100%)"></div>
</section>

<!-- Principles -->
<section class="slide col-l row-2">
  <div class="glow" style="left:170px;top:60px;width:200px;height:90px;background:radial-gradient(ellipse,rgba(213,154,78,.4),transparent 70%);transform:rotate(-20deg)"></div>
  <div class="glow" style="left:-30px;top:-20px;width:200px;height:60px;background:radial-gradient(ellipse,rgba(213,154,78,.3),transparent 70%)"></div>
  <h2 class="abs heading" style="left:37px;top:25px;font-size:23px">Our Sponsorship Principles</h2>
  <div class="card principle" style="left:37px;top:65px;width:147px;height:49px"><span class="num">01</span><p>It is envisaged the sponsorship must provide benefits to members of the Harrowfield Bowls Union generally however it can be aligned to specific properties either listed but not limited to that list. Further thoughts / ideas can be discussed.</p></div>
  <div class="card principle" style="left:191px;top:65px;width:149px;height:49px"><span class="num">02</span><p>Sponsorship may be provided and recognised in the form of : cash donation; valued business or personal expertise required by the club; agreed supply of product or equipment required by the club in the provision of our duties.</p></div>
  <div class="card principle" style="left:37px;top:121px;width:147px;height:37px"><span class="num">03</span><p>Sponsorships can be contracted on a season by season basis however we seek sponsorship generally on a 3 year basis with a mutual review annually.</p></div>
  <div class="card principle" style="left:191px;top:121px;width:149px;height:37px"><span class="num">04</span><p>Acceptance of sponsorship within each agreed package indicates the Harrowfield Bowls Union support for the sponsor and / or their business.</p></div>
  <div class="card principle" style="left:37px;top:165px;width:303px;height:26px"><span class="num">05</span><p>We promote only one sponsorship in each category of business (eg Banking Services / Food Services).</p></div>
</section>

<!-- Why -->
<section class="slide col-r row-2">
  <div class="glow" style="left:250px;top:-20px;width:160px;height:60px;background:radial-gradient(ellipse,rgba(213,154,78,.45),transparent 70%)"></div>
  <div class="glow" style="left:100px;top:160px;width:140px;height:60px;background:radial-gradient(ellipse,rgba(213,154,78,.35),transparent 70%)"></div>
  <h2 class="abs heading" style="left:18px;top:25px;font-size:23px">Why Harrowfield Bowls Union?</h2>
  <div class="abs body" style="left:19px;top:63px;width:300px">Harrowfield Bowls Union is one of Australia's oldest and most respected cricket clubs.<br>Founded in 1897, we are a not-for-profit organisation dedicated to growing cricket across our city and state .</div>
  <div class="abs sub" style="left:19px;top:84px">Every dollar generated through sponsorship is reinvested directly into :</div>
  <div class="card" style="left:19px;top:98px;width:177px;height:53px;padding:9px 8px;display:flex;gap:8px">
    <ul class="list" style="flex:1"><li>Men's and Women's Premier Cricket</li><li>Junior Development Programs</li><li>Community Coaching</li></ul>
    <ul class="list" style="flex:1"><li>Youth Academies</li><li>Female Participation</li><li>Multicultural Cricket</li><li>Facilities at Kestrel Park Oval</li></ul>
  </div>
  <div class="photo" role="img" aria-label="Men's team celebrating with champions banner" style="left:206px;top:98px;width:158px;height:130px;background:linear-gradient(180deg,#9aa38a 0%,#4a4a3a 35%,#1e1c18 65%,#4c6a2f 100%)"></div>
  <div class="abs body" style="left:19px;top:161px;width:180px">Unlike many sponsorships, your investment doesn't simply buy hospitality.</div>
  <div class="abs body" style="left:19px;top:174px;width:180px">It helps create opportunities for hundreds of young cricketers while connecting your business with one of Australia's most iconic sporting institutions.</div>
</section>

<!-- Highlights -->
<section class="slide col-l row-3">
  <div class="glow" style="left:220px;top:-10px;width:180px;height:60px;background:radial-gradient(ellipse,rgba(213,154,78,.35),transparent 70%)"></div>
  <div class="glow" style="left:-40px;top:150px;width:120px;height:90px;background:radial-gradient(ellipse,rgba(213,154,78,.3),transparent 70%)"></div>
  <h2 class="abs heading" style="left:18px;top:15px;font-size:23px">Recent Team<br>highlights</h2>
  <div class="abs" style="left:18px;top:75px;width:175px">
    <div class="sub">Our Recent Success Men</div>
    <ul class="list" style="margin-top:4px">
      <li>2020 -Our men's T20 team was crowned national champions last year winning the National Cricket Board tournament in Adelaide.</li>
      <li>2021 -Our Men's 1st grade Premier team won the Metro Cricket Premiership.</li>
      <li>2022 -Our Men's T20 team won the Metro Cricket Association T20 Championship</li>
    </ul>
    <div class="sub" style="margin-top:7px">Our Recent Success Women</div>
    <ul class="list" style="margin-top:4px">
      <li>2020 -Our Women's 1st Grade and U/18 won the Metro Cricket Premierships.</li>
      <li>2021 -Our Women's Division were Club Champions.</li>
      <li>2020 -Our Women's 1st Grade and U/18 won the Metro Cricket Premierships.</li>
      <li>2022 -Our Women's Division our 1stGrade were T20 Champions, 2ndGrade and Brewers were Premiership Champions, and the Women's club were Club Champions.</li>
      <li>2023 - Our Women's 1stGrade were Premiership and T20 Champions.</li>
      <li>Kestrel Park Oval rated one of the city's best grounds and has recently hosted State 4 Day Games and Premier Cricket 1st Grade Grand Finals.</li>
    </ul>
  </div>
  <div class="photo" role="img" aria-label="Women's first grade T20 premiers celebrating with banner and trophy" style="left:200px;top:53px;width:167px;height:142px;background:linear-gradient(180deg,#8a9a9a 0%,#3a3a30 35%,#22252e 60%,#2f4f8a 75%,#4f7a3a 100%)"></div>
</section>

<!-- Snapshot -->
<section class="slide col-r row-3">
  <div class="glow" style="left:-20px;top:-10px;width:140px;height:60px;background:radial-gradient(ellipse,rgba(213,154,78,.4),transparent 70%)"></div>
  <div class="glow" style="left:300px;top:50px;width:100px;height:90px;background:radial-gradient(ellipse,rgba(213,154,78,.3),transparent 70%)"></div>
  <h2 class="abs heading" style="left:24px;top:35px;font-size:22.5px">Snapshot - Our History Drives<br>Our Current Success</h2>
  <div class="card body" style="left:24px;top:97px;width:170px;height:81px;padding:7px 8px;font-size:3.8px;line-height:1.55">Our women's division has an unparalleled "representative honor board". Current State Breakers and Australian Internationals, Mara Quinlan and Tessa Marlow; Jodie Renner; former Australian Internationals Fiona Galt AO; Helen Strode; Wendy Aske and current England women's coach, Kate Borland are only a few who have called Kestrel Park Oval home. The club takes "grass roots" cricket very seriously supporting local competitions and youth representative cricketers through the provision of coaching academies. The academies are provided to local community cricketers at no cost on the best facilities with qualified coaches 300 players and families from the inner west utilise the Kestrel Park Oval facilities each week.</div>
  <div class="photo" role="img" aria-label="Team huddle seen from below against the sky" style="left:207px;top:97px;width:154px;height:130px;border-radius:9px 9px 0 0;background:linear-gradient(180deg,#f2f2f0 0%,#d8d8d4 40%,#2a2824 70%,#1a1814 100%)"></div>
</section>

<!-- Committee -->
<section class="slide col-l row-4">
  <div class="glow" style="left:-30px;top:-20px;width:160px;height:70px;background:radial-gradient(ellipse,rgba(213,154,78,.4),transparent 70%)"></div>
  <div class="glow" style="left:260px;top:100px;width:140px;height:80px;background:radial-gradient(ellipse,rgba(213,154,78,.3),transparent 70%)"></div>
  <h2 class="abs heading" style="left:0;top:14px;width:387px;text-align:center;font-size:21.5px">Harrowfield Bowls Union (est.<br>1897) Committee Structure</h2>
  <svg class="abs" style="left:0;top:0" width="387" height="218" viewBox="0 0 387 218" aria-hidden="true">
    <g stroke="#cfc8bd" stroke-width=".5" fill="none">
      <path d="M194 98v11"/><path d="M194 125v10M96 135h197M96 135v10M161 135v10M229 135v10M293 135v10"/>
      <path d="M96 164v10M43 174h106M43 174v9M96 174v9M149 174v9"/>
    </g>
    <g fill="#cfc8bd"><path d="M192.5 108l1.5 2 1.5-2z"/><path d="M94.5 144l1.5 2 1.5-2zM159.5 144l1.5 2 1.5-2zM227.5 144l1.5 2 1.5-2zM291.5 144l1.5 2 1.5-2z"/><path d="M41.5 182l1.5 2 1.5-2zM94.5 182l1.5 2 1.5-2zM147.5 182l1.5 2 1.5-2z"/></g>
  </svg>
  <div class="node" style="left:113px;top:75px;width:161px;height:23px">Ross Pemberton (Chair); Neil Ardley, Phil Carrow; Martin Oakes Dean Tolley,<br>Janet Sorell; Matt Prideaux, Greg Hollis, Gina Pellow BOARD</div>
  <div class="node" style="left:155px;top:110px;width:79px;height:15px">Stuart Thornbury General Manager</div>
  <div class="node" style="left:72px;top:146px;width:48px;height:18px">TBC Director of<br>Coaching</div>
  <div class="node" style="left:133px;top:146px;width:56px;height:18px">Karl Benning<br>Operations Manager</div>
  <div class="node" style="left:203px;top:146px;width:53px;height:18px">Gavin Zeller<br>Women's Chairman</div>
  <div class="node" style="left:269px;top:146px;width:48px;height:18px">Linda Morrow<br>HGS XI</div>
  <div class="node" style="left:20px;top:184px;width:47px;height:18px">Ben Sauer Head<br>Coach Mens</div>
  <div class="node" style="left:72px;top:184px;width:48px;height:18px">Michael Hume Head<br>Coach Women</div>
  <div class="node" style="left:126px;top:184px;width:47px;height:18px">TBC Academy's<br>Coach</div>
</section>

<!-- Testimonial -->
<section class="slide col-r row-4">
  <div class="glow" style="left:300px;top:110px;width:110px;height:110px;background:radial-gradient(ellipse,rgba(213,154,78,.4),transparent 70%)"></div>
  <h2 class="abs heading" style="left:24px;top:20px;font-size:23px">Testimonial</h2>
  <div class="card" style="left:24px;top:57px;width:281px;height:72px;padding:8px 10px">
    <p class="body" style="font-size:3.8px;line-height:1.6">"Harrowfield Bowls Union is one of the oldest and proudest clubs in the Metro Premier Cricket Competition. A club with over 140 playing members across both women's and men's divisions. Arguably one of the city's most successful clubs in the last 10 years on the field with over 10 premierships including a Women's 1st grade premiership 2019/20, Men's 1st grade premiership 2020/21, Women's Club Championship 2020/21, Men's National T20 premiers 2019/20 just to name a few. Our on-field success is a credit to the hard-working individuals and volunteers that this club is indebted to. With a strong tie in the community with hundreds of junior cricketers coming through in our junior coaching programs and junior teams, Harrowfield Bowls Union is keen on growing in the community to help nurture cricket in the entire inner west and city. Your support will allow us to grow the game and produce the next Mara Quinlan"</p>
    <p class="sub" style="font-size:3.8px;margin-top:4px">Ross Pemberton – Chairman Harrowfield Bowls Union</p>
  </div>
  <div class="sponsors" style="left:24px;top:136px;width:229px;height:61px">
    <span class="sponsor">Orchard Lane</span>
    <span class="sponsor">Halden Council</span>
    <span class="sponsor">Brightwell</span>
    <span></span>
    <span class="sponsor">Corvid Freight</span>
    <span class="sponsor">Ashgrove</span>
    <span class="sponsor">Regional Sport</span>
    <span class="sponsor">Sport Board</span>
  </div>
</section>

<!-- Proposal summary -->
<section class="slide col-l row-5">
  <div class="glow" style="left:250px;top:-20px;width:150px;height:80px;background:radial-gradient(ellipse,rgba(213,154,78,.4),transparent 70%)"></div>
  <div class="glow" style="left:300px;top:150px;width:110px;height:80px;background:radial-gradient(ellipse,rgba(213,154,78,.3),transparent 70%)"></div>
  <div class="photo" role="img" aria-label="Two club members holding a trophy on a cricket ground" style="left:26px;top:31px;width:141px;height:161px;background:linear-gradient(180deg,#b9b4a8 0%,#8c7a5a 30%,#c9a63a 55%,#5d8a3a 80%,#4a7a30 100%)"></div>
  <h2 class="abs heading" style="left:179px;top:28px;font-size:23.5px">Proposal<br>Summary</h2>
  <div class="card body" style="left:179px;top:90px;width:175px;height:41px;padding:8px 7px;font-size:3.9px">Our Sponsorship Principles are listed on page 22 (Appendix) this information pack and we aim to fully engage and recognize our valued sponsors. Whichever package you choose goes to helping this community cricket club and its members, in supporting their passion. Thank you for your consideration.</div>
  <div class="abs sub" style="left:179px;top:146px;font-size:5.5px">Contact General Manager</div>
  <div class="abs contact" style="left:179px;top:159px">Stuart Thornbury<br>Harrowfield Bowls Union<br>Tel: 0400 000 123<br>Email: stuart.thornbury@hbu-club.example</div>
</section>

<!-- Thank you -->
<section class="slide col-r row-5">
  <div class="glow" style="left:-20px;top:40px;width:120px;height:90px;background:radial-gradient(ellipse,rgba(213,154,78,.35),transparent 70%)"></div>
  <div class="glow" style="left:200px;top:130px;width:170px;height:70px;background:radial-gradient(ellipse,rgba(213,154,78,.45),transparent 70%);transform:rotate(-20deg)"></div>
  <div class="glow" style="left:290px;top:-20px;width:120px;height:60px;background:radial-gradient(ellipse,rgba(213,154,78,.3),transparent 70%)"></div>
  <h2 class="abs heading" style="left:0;top:66px;width:387px;text-align:center;font-size:51px;letter-spacing:-.05em">Thank You</h2>
  <div class="presented" style="top:187px">Presented by :<b>HARROWFIELD BOWLS UNION</b></div>
</section>

</body>
</html>
```